Brightwell Pictures Business Card

Hello,

i would like to have a dynamic, creative but tasteful card, colour used, front and back. I have attached a sample card that I liked very much from another individual to give you an idea of the theme/approach, but not colour. Ideally the graphic elements of the Brightwell Logo are brought into the design.

Target Market(s)

North America

Industry/Entity Type

Film Production

Contact Information for Business Card

Mirela Vantasch
President/Founder
Brightwell Pictures Inc.
587 914 3362
mirela@brightwellpix.tv

Font styles to use
Sans Serif

Colors
6b449b
5c5c5c
fdfdfd
000000

Requirements
Must have
• Logo, name, Company name, email and cell number. no Address line to be included.
Should not have
• any unrelated GFX elements, serif fonts

```html
<!DOCTYPE html>
<html lang="en">
<head>
<meta charset="utf-8">
<title>Brightwell Pictures – Business Card</title>
<link href="https://fonts.googleapis.com/css2?family=Arimo:wght@400;700&display=swap" rel="stylesheet">
<style>
  :root {
    --purple: #6b449b;
    --purple-deep: #5a2f96;
    --lavender: #b9a6d6;
    --grey: #5c5c5c;
    --text: #333333;
    --icon: #2c2a6e;
    --paper: #fdfdfd;
    --ink: #000000;
    --backdrop: #e9e8ec;
  }
  * { box-sizing: border-box; margin: 0; padding: 0; }
  html, body {
    width: 1200px; height: 907px; overflow: hidden;
    background: var(--backdrop);
    font-family: "Arimo", Arial, sans-serif;
  }
  .canvas { position: relative; width: 1200px; height: 907px; }
  .card {
    position: absolute; top: 299px;
    width: 540px; height: 309px;
    border-radius: 22px;
    background: var(--paper);
    overflow: hidden;
    box-shadow: 0 10px 30px rgba(0,0,0,.18);
  }
  .card--front { left: 40px; }
  .card--back { left: 620px; }

  .wordmark {
    font-weight: 700; color: var(--grey);
    letter-spacing: -0.5px; line-height: 1;
  }

  /* front */
  .ring-field {
    position: absolute; inset: 0;
    background: radial-gradient(circle at 50% 50%, var(--purple-deep) 0 38%, var(--lavender) 52%, var(--purple) 68%, var(--lavender) 100%);
  }
  .front-disc {
    position: absolute; left: 145px; top: 30px;
    width: 250px; height: 250px; border-radius: 50%;
    background: var(--paper);
    box-shadow: 0 0 0 10px var(--paper), 0 0 0 22px var(--purple-deep);
    display: flex; align-items: center; justify-content: center;
  }
  .front-disc .wordmark { font-size: 34px; }

  /* back */
  .back-rings {
    position: absolute; right: -40px; top: -60px;
    width: 300px; height: 300px; border-radius: 50%;
    background: radial-gradient(circle, var(--purple) 0 28%, var(--paper) 29% 32%, var(--purple-deep) 33% 46%, var(--lavender) 60%, rgba(185,166,214,0.3) 80%, rgba(253,253,253,0) 100%);
  }
  .back-content { position: absolute; left: 38px; top: 110px; }
  .back-content .wordmark { font-size: 40px; margin-bottom: 24px; }
  .person-name { font-size: 17px; font-weight: 700; color: #3a3a3a; line-height: 1.2; }
  .person-role { font-size: 13px; color: var(--purple); line-height: 1.3; margin-bottom: 8px; }
  .company { font-size: 12px; color: var(--text); line-height: 1.3; margin-bottom: 8px; }
  .contact { display: flex; align-items: center; gap: 7px; font-size: 12px; color: var(--text); line-height: 1.5; }
  .contact svg { width: 13px; height: 13px; flex: none; }
</style>
</head>
<body>
<main class="canvas">
  <section class="card card--front" aria-label="Card front">
    <div class="ring-field" role="img" aria-label="Concentric purple and lavender arc segments radiating around the centre"></div>
    <div class="front-disc">
      <span class="wordmark">Brightwell</span>
    </div>
  </section>

  <section class="card card--back" aria-label="Card back">
    <div class="back-rings" role="img" aria-label="Purple and lavender arc segments radiating in the upper right corner"></div>
    <div class="back-content">
      <p class="wordmark">Brightwell</p>
      <p class="person-name">Mirela Vantasch</p>
      <p class="person-role">President/Founder</p>
      <p class="company">Brightwell Pictures Inc.</p>
      <p class="contact">
        <svg viewBox="0 0 16 16" aria-hidden="true"><circle cx="8" cy="8" r="8" fill="var(--icon)"/><path d="M5.2 4.5l1.4-.3.8 1.8-.9.7c.5 1 1.3 1.8 2.3 2.3l.7-.9 1.8.8-.3 1.4c-3 .2-6-2.8-5.8-5.8z" fill="#fff"/></svg>
        587 914 3362
      </p>
      <p class="contact">
        <svg viewBox="0 0 16 16" aria-hidden="true"><circle cx="8" cy="8" r="8" fill="var(--icon)"/><rect x="4" y="5.2" width="8" height="5.6" fill="#fff"/><path d="M4 5.2l4 3 4-3" fill="none" stroke="var(--icon)" stroke-width="0.9"/></svg>
        mirela@brightwellpix.tv
      </p>
    </div>
  </section>
</main>
</body>
</html>
```